Business card - house cleaning company

We want friendly high end business card highlighting our services . NO LOGOs on back of card please.. no vertical cards NO DOUBLE BROOMS

2 owners of the company: Corinne Halvey & Joel Brandt

Included phone number: (555)318-2047

Email: brightlanetidy@mailnest.example

Website: www.brightlanetidy.example

Bonded & Insured

Estes Park, CO 80517

Slogan maybe: Bringing a brighter shine to every corner of home

We want elegant high end card for house cleaning service. Maybe 2 sided if needed. Can it have bullet points of some services we offer

Residential Home Cleaning
Vacation Rental Cleaning
Commercial Cleaning
Carpet Cleaning
Window Cleaning
Property Management
Property Inspections
Property Maintenance
Trash Removal
Concierge Services

Highlight service on back of card. If we can do a one sided card with all this that’s great as well. Not cartoony.

Our logo attached and a design somone I had Perrin but they put very little time in. Not Unique enough. If you can do a custom design with a feminine touch that be great.

You will be eliminated for not reading the brief. NO DOUBLE LOGOS NO DOUBLE BROOMS. PLEASE BE CREATIVE. IF POST SAME LOGO WITH SMAL CHANGES RHEY WILL BE ELIMINATED. BE CREATIVE.

Thank you everyone for your designs. please only use the logo 1 time. and would love to see some that dont look all the same. We appreciate your time.

Target Market(s)

Residential and vacation rental home cleaning maid service

Industry/Entity Type

House cleaning maid services

Contact Information for Business Card

For business card use logo. black and green one provided. others for example. I wil try find some example.. We want friendly high end look. 2 owners of the company: Corinne Halvey & Joel Brandt Included phone number: (555)318-2047 Email: brightlanetidy@mailnest.example Website: www.brightlanetidy.example Bonded & Insured Estes Park, CO Slogan maybe: Bringing a brighter shine to every corner of home or Quality Service Guaranteed We want elegant high end card for house cleaning service. Maybe 2 sided if needed. Can it have bullet points of some services we offer Residential Home Cleaning Vacation Rental Cleaning Commercial Cleaning Carpet Cleaning Window Cleaning Property Management Property Inspections Property Maintenance Trash Removal Concierge Services

Requirements
Must have
• For business card use logo . Creativity. black and green one provided. We want friendly high end look. 2 owners of the company: Corinne Halvey & Joel Brandt Included phone number: (555)318-2047 Email: brightlanetidy@mailnest.example Website: www.brightlanetidy.example Licensed Bonded & Insured Estes Park, CO Slogan maybe: Bringing a brighter shine to every corner of home or Quality Service Guaranteed We want elegant high end card for house cleaning service. Maybe 2 sided if needed. Can it have bullet points of some services we offer Residential Home Cleaning Vacation Rental Cleaning Commercial Cleaning Carpet Cleaning Window Cleaning Property Management Property Inspections Property Maintenance Trash Removal Concierge Services .. creatitivty a plus. whimsical. we like stars..
Nice to have
• we want much better than the example of biz card provided as example. logo has colors that are in our website palette as well. We are open to ideas for the business card design. Will pay tip to best work. PLEASE USE COMPLIMENTING COLORS. . WE LIKE BLACK AND WHITE, stars
Should not have
• NO DOUBLE LOGOS. READ READ. READ. YOU WILL BE ELIMINATED no double logos or double brooms same side of card. I want didfrent examples. please don't make all your submission look the same

```html
<!DOCTYPE html>
<html lang="en">
<head>
<meta charset="utf-8">
<title>Bright Lane Tidy – Business Card</title>
<link rel="stylesheet" href="https://fonts.googleapis.com/css2?family=EB+Garamond:ital,wght@0,400;0,600;0,700;1,400;1,600&display=swap">
<style>
  :root{
    --bg:#dcdcdd;
    --paper:#ffffff;
    --green:#6e9645;
    --ink:#141414;
    --charcoal:#2c2c2d;
    --white:#ffffff;
  }
  *{box-sizing:border-box;margin:0;padding:0}
  html,body{width:1200px;height:800px;overflow:hidden}
  body{
    background:var(--bg);
    font-family:"EB Garamond",Georgia,serif;
    position:relative;
  }
  .card{
    position:absolute;top:246px;
    width:540px;height:309px;
    border-radius:18px;overflow:hidden;
  }
  .card--front{left:40px;background:var(--paper)}
  .card--back{
    left:620px;background:var(--charcoal);
    display:flex;align-items:center;justify-content:center;
  }

  .card__art{position:absolute;inset:0}

  .brand{
    position:absolute;left:34px;top:82px;
    display:flex;align-items:center;gap:10px;
  }
  .brand__dot{width:13px;height:13px;border-radius:50%;background:var(--green)}
  .brand__name{font-size:30px;font-weight:700;color:var(--ink);line-height:1}

  .owners{position:absolute;left:36px;top:178px}
  .owners__names{font-size:22px;font-weight:700;color:var(--green);line-height:1.1}
  .owners__title{font-size:13px;font-style:italic;color:var(--ink);margin-top:4px}

  .contact{
    position:absolute;right:22px;top:34px;
    text-align:right;color:var(--white);
    font-size:12.5px;line-height:1.5;font-style:normal;
  }

  .services{
    text-align:center;color:var(--white);
    font-size:15px;line-height:1.6;
  }
  .services__sep{color:var(--green);font-weight:700;margin:0 6px}
</style>
</head>
<body>

<section class="card card--front" aria-label="Business card front">
  <svg class="card__art" viewBox="0 0 540 309" width="540" height="309">
    <polygon points="200,309 360,0 540,0 540,309" fill="var(--green)"/>
    <g fill="var(--ink)">
      <path d="M322 10 l4 10 10 4 -10 4 -4 10 -4 -10 -10 -4 10 -4z"/>
      <path d="M300 22 l3 7 7 3 -7 3 -3 7 -3 -7 -7 -3 7 -3z"/>
      <path d="M282 52 l3 7 7 3 -7 3 -3 7 -3 -7 -7 -3 7 -3z"/>
    </g>
    <path d="M428 140 l3 8 8 3 -8 3 -3 8 -3 -8 -8 -3 8 -3z" fill="var(--white)"/>
    <g transform="translate(219 296) rotate(-62.6)">
      <rect x="0" y="-10" width="195" height="20" rx="10" fill="var(--ink)"/>
      <text x="97.5" y="3.5" text-anchor="middle" font-family="EB Garamond, serif" font-style="italic" font-weight="600" font-size="9" fill="var(--green)">Bringing a brighter shine to every corner of home</text>
    </g>
  </svg>

  <div class="brand">
    <span class="brand__dot"></span>
    <span class="brand__name">Bright Lane Tidy</span>
  </div>

  <div class="owners">
    <p class="owners__names">Corinne Halvey &amp;<br>Joel Brandt</p>
    <p class="owners__title">President</p>
  </div>

  <address class="contact">
    (555)318-2047<br>
    brightlanetidy@mailnest.example<br>
    www.brightlanetidy.example<br>
    Estes Park, CO 80517
  </address>
</section>

<section class="card card--back" aria-label="Business card back">
  <p class="services">
    Residential Home Cleaning<span class="services__sep">+</span>Vacation Rental Cleaning<br>
    Commercial Cleaning<span class="services__sep">+</span>Carpet Cleaning<span class="services__sep">+</span>Window Cleaning<br>
    Property Management<span class="services__sep">+</span>Property Inspections<span class="services__sep">+</span>Property Maintenance<br>
    Trash Removal<span class="services__sep">+</span>Concierge Services
  </p>
</section>

</body>
</html>
```